"Marvels Unbound" Super Hero Characters

We are launching a new website called Marvels Unbound, based on the work of the real world scientists, Dr Lena Marsh and her husband, Dr. Paul Orwick. The focus of the site is exploring and discovering the "impossible" in ourselves and the world around us.

You can learn more about the project at www.marvelsunbound-example.com/home

We are looking to create super-hero-esque caricatures for both Dr Marsh and Dr Orwick. We want the caricatures to bear a resemblance to both of the real life doctors, but have a super-hero-like appearance. We also want to make sure that they have an element of science to them to reflect their "Doctor" brand.

Once we establish base caricatures for each Doctor, we will want to have 4-5 different versions with them in different poses, etc that we can use in different places on the website.

We've attached real life pictures of both doctors here. You can also take a look at the website (www.marvelsunbound-example.com/home) to get a sense of the web environment in which they will "live." The superhero characters that are currently on the site are merely placeholders for the new ones you will design. . . and aren't necessarily guides for the illustrations.

Industry/Entity Type

Work

Font styles to use
Sans Serif

Colors

Designer to choose colors to be used in the design.

Requirements
Must have
• Caricatures must resemble the real life doctors.
• They must have a "sciency" feel
• They must be fun
Should not have
• The caricatures must not be generic or feel like "stock" images.

```html
<!DOCTYPE html>
<html lang="en">
<head>
<meta charset="utf-8">
<title>Personal – Marvels Unbound</title>
<link href="https://fonts.googleapis.com/css2?family=Open+Sans:wght@400;600&display=swap" rel="stylesheet">
<style>
  :root {
    --page-bg: #ffffff;
    --heading: #2b2b2b;
    --body-text: #666666;
    --nav-text: #666666;
    --nav-active: #2ea3f2;
    --rule: #ececec;
    --art-light: #fafafa;
    --art-mid: #d2d2d2;
    --art-dark: #9a9a9a;
  }
  * { box-sizing: border-box; margin: 0; padding: 0; }
  html, body {
    width: 1200px;
    height: 800px;
    overflow: hidden;
    background: var(--page-bg);
    font-family: "Open Sans", Arial, sans-serif;
  }
  .page {
    position: relative;
    width: 1200px;
    height: 800px;
  }
  .site-header {
    position: absolute;
    left: 0;
    top: 0;
    width: 1200px;
    height: 66px;
    box-shadow: 0 1px 0 var(--rule);
  }
  .main-nav {
    position: absolute;
    left: 350px;
    top: 0;
    height: 66px;
    display: flex;
    align-items: center;
    gap: 32px;
  }
  .nav-link {
    font-size: 16px;
    font-weight: 600;
    color: var(--nav-text);
    text-decoration: none;
    display: flex;
    align-items: center;
    gap: 7px;
  }
  .nav-link--active { color: var(--nav-active); }
  .nav-caret { width: 10px; height: 7px; }
  .brand {
    display: flex;
    align-items: center;
    gap: 9px;
    font-size: 16px;
    font-weight: 400;
    color: var(--nav-text);
  }
  .brand-mark {
    width: 30px;
    height: 30px;
    border: 1.5px solid var(--nav-text);
    border-radius: 50%;
  }
  .search-icon { width: 19px; height: 19px; }
  .intro {
    position: absolute;
    left: 26px;
    top: 142px;
    width: 580px;
  }
  .intro-title {
    font-size: 41px;
    font-weight: 400;
    line-height: 1.03;
    color: var(--heading);
    margin-bottom: 14px;
  }
  .intro-text {
    font-size: 18.5px;
    line-height: 31px;
    color: var(--body-text);
    margin-bottom: 16px;
  }
  .hero-art {
    position: absolute;
    left: 666px;
    top: 160px;
    width: 380px;
    height: 462px;
    background:
      radial-gradient(ellipse 46% 48% at 50% 52%, var(--art-dark) 0%, var(--art-mid) 45%, var(--art-light) 80%, var(--page-bg) 100%);
  }
</style>
</head>
<body>
<div class="page">
  <header class="site-header">
    <nav class="main-nav">
      <a class="nav-link" href="#">Home</a>
      <a class="nav-link" href="#">About
        <svg class="nav-caret" viewBox="0 0 11 7"><path d="M1 1l4.5 4.5L10 1" fill="none" stroke="currentColor" stroke-width="1.8"/></svg>
      </a>
      <div class="brand"><span class="brand-mark"></span>Marvels Unbound</div>
      <a class="nav-link nav-link--active" href="#">Explore
        <svg class="nav-caret" viewBox="0 0 11 7"><path d="M1 1l4.5 4.5L10 1" fill="none" stroke="currentColor" stroke-width="1.8"/></svg>
      </a>
      <a class="nav-link" href="#">Sixth Sense Quiz</a>
      <svg class="search-icon" viewBox="0 0 20 20" aria-label="Search"><circle cx="11.5" cy="8.5" r="6" fill="none" stroke="#555" stroke-width="1.8"/><path d="M7.2 12.8L2 18" stroke="#555" stroke-width="1.8" stroke-linecap="round"/></svg>
    </nav>
  </header>

  <section class="intro">
    <h1 class="intro-title">There is a treasure trove of hidden abilities inside each of us.</h1>
    <p class="intro-text">In fact, within our bodies and minds resides the building blocks for the humans of the future. Whether it’s hyper-sensitive smell, the ability to visualize abstract ideas, or draw with surprising accuracy, each of us holds skills and talents that we often overlook, but that could be used to better our own lives and give us a glimpse of what’s possible.</p>
    <p class="intro-text">Below are a series of quizzes, exercises, factoids, and articles that will help you to get acquainted with your inner extraordinary. Enjoy!</p>
  </section>

  <div class="hero-art" role="img" aria-label="Pencil-sketch caricatures of Dr Lena Marsh and Dr. Paul Orwick as playful superhero scientists in long lab coats, standing side by side"></div>
</div>
</body>
</html>
```